Vocational Mentor needs an impressive business card

1. I need a business card (or maybe three with identic look) to promote me and my three business titles/services:
- Vocational Mentor. I help people find their vocation and live happily from it. I use my 20 years of experience in business, management and psychology to help them identify the most efficient ways to make a living doing what they are passionate about.
- Business Angel. I help founders start a succesful business with minimum risks and costs. I use my 20 years of experience in sales, management and entrepreneurship to help them identify the most efficient ways, in terms of time and cost, to validate their business idea.
- Learning Designer. I design unique learning programs that produce long-term cognitive and behavioural changes to people and organisations. I use my 20 years of experience in learning, teaching and change management to create minimalist experiences and processes that allow them to change efficiently in their pursued direction.

2. I would like a two-sided business card, on the front with my name, contact details and titles, on the back the explanation of the services.
Updates

Hi all,

I updated my brief, included contacts info and give feedback on all designs I got. I am new on this platform so please tell me if you need anything else or if I don't use corectly the platform forms.

Kind regards,
Mirel

Hi all,

I shortened the services description by deleting the phrase "I call..."

Kind regards,
Mirel

Target Market(s)

Freelancers, startups, people and organization willing to invest in change through ultimate learning experiences

Industry/Entity Type

Business

Font styles to use
Serif

Requirements
Must have
• Front side: full name, titles, web site, email, phone like below:
Mirel Vantaru
Vocational Mentor, Business Angel, Learning Designer
info@mirelvantaru.example
www.mirelvantaru.example
+40-748-MIRELV
Nice to have
• Back side: the description of the services I provide as in the task description.
1/3: it would be nice if I can jam all three titles on the front side but then I need a solution to jam all three services on the back side.

```html
<!DOCTYPE html>
<html lang="en">
<head>
<meta charset="utf-8">
<title>Mirel Vantaru – Business Card</title>
<link rel="stylesheet" href="https://fonts.googleapis.com/css2?family=Sorts+Mill+Goudy&display=swap">
<style>
  :root {
    --page-bg: #ffffff;
    --card-navy: #1e2061;
    --card-edge: #4a4a4a;
    --name-orange: #f08a2e;
    --rule-orange: #d4532a;
    --text-white: #ffffff;
  }
  html, body {
    margin: 0;
    padding: 0;
    width: 726px;
    height: 1200px;
    overflow: hidden;
    background: var(--page-bg);
  }
  .card {
    position: absolute;
    left: 2px;
    top: 2px;
    width: 718px;
    height: 1194px;
    box-sizing: border-box;
    overflow: hidden;
    background: var(--card-navy);
    border: 2px solid var(--card-edge);
    border-radius: 62px;
    font-family: "Sorts Mill Goudy", "Times New Roman", serif;
    color: var(--text-white);
  }
  .card > * {
    position: absolute;
    margin: 0;
    line-height: 1;
    white-space: nowrap;
    font-weight: 400;
    text-align: center;
  }
  .holder-name {
    left: 10px;
    width: 694px;
    top: 323px;
    font-size: 56px;
    text-transform: uppercase;
    color: var(--name-orange);
  }
  .holder-title {
    left: 0;
    width: 702px;
    top: 390px;
    font-size: 44px;
  }
  .contact-rule {
    left: 61px;
    top: 773px;
    width: 624px;
    height: 2px;
    background: var(--rule-orange);
  }
  .contact {
    left: 8px;
    width: 702px;
    font-size: 43px;
  }
  .contact-email { top: 792px; }
  .contact-web   { top: 861px; }
  .contact-phone { top: 932px; font-size: 46px; }
</style>
</head>
<body>
  <div class="card">
    <h1 class="holder-name">Mirel Vantaru</h1>
    <p class="holder-title">Business Angel</p>
    <div class="contact-rule"></div>
    <p class="contact contact-email">info@mirelvantaru.example</p>
    <p class="contact contact-web">www.mirelvantaru.example</p>
    <p class="contact contact-phone">+40-748-MIRELV</p>
  </div>
</body>
</html>
```